Industrial & commercial facility maintenance flyer

Design a 2 sided flyer that outlines our core business unit services. One side shall be for our industrial maintenance division while the other will be focused on our commercial maintenance division.

Media from website here: https://files.velnorashare.com/folders/7K3QzP91mXwRtLaBvYcNe4HdUsFj

Target Market(s)

Industrial and commercial facility maintenance companies and professionals

Industry/Entity Type

Maintenance

Font styles to use
Serif

Colors
ffffff
2f73b4
0455a3
cfdfed

Requirements
Must have
• Several photos of each applicable service. Reference existing website (www.tkrvb.com). Use of the blue and grey scheme of our current logo.
Nice to have
• Our logo design across the top with our contact information on the bottom.

```html
<!DOCTYPE html>
<html lang="en">
<head>
<meta charset="utf-8">
<title>Harbor Facility Solutions – Retail &amp; Commercial Maintenance Flyer</title>
<link rel="stylesheet" href="https://fonts.googleapis.com/css2?family=Bebas+Neue&family=Raleway:wght@300;400;600;700&display=swap">
<style>
  :root {
    --white: #ffffff;
    --blue-mid: #2f73b4;
    --blue-deep: #0455a3;
    --blue-pale: #cfdfed;
    --blue-head: #1b57a6;
    --grey-band: #c9cbce;
    --grey-text: #444a52;
    --stage: #e4e4e4;
  }
  * { margin: 0; padding: 0; box-sizing: border-box; }
  html, body { width: 970px; height: 1200px; overflow: hidden; background: var(--stage); }
  body { font-family: "Raleway", sans-serif; }

  .flyer {
    position: absolute; left: 60px; top: 0;
    width: 850px; height: 1200px;
    background: var(--white); overflow: hidden;
  }
  .flyer__shapes { position: absolute; inset: 0; width: 850px; height: 1200px; }

  .headline { position: absolute; right: 55px; top: 58px; text-align: right; color: #2d3238; }
  .headline__lead { font-family: "Raleway", sans-serif; font-weight: 600; font-size: 27px; line-height: 44px; }
  .headline__big { font-family: "Bebas Neue", sans-serif; color: var(--blue-head); font-size: 50px; letter-spacing: 0.5px; vertical-align: -3px; }
  .headline__main { font-family: "Bebas Neue", sans-serif; color: var(--blue-head); font-size: 50px; line-height: 46px; letter-spacing: 0.3px; }
  .headline__sub { font-weight: 600; font-size: 28px; line-height: 38px; }
  .headline__tag { font-weight: 600; font-size: 14.5px; line-height: 24px; }
  .headline__rule { position: absolute; right: 55px; top: 212px; width: 189px; height: 4px; background: var(--blue-head); }

  .section-title { position: absolute; right: 76px; top: 243px; text-align: right; }
  .section-title__light { font-weight: 300; font-size: 31px; color: #3d4249; line-height: 33px; }
  .section-title__bold { font-weight: 700; font-size: 30px; color: var(--blue-head); line-height: 33px; }
  .section-title__bar { position: absolute; right: 55px; top: 250px; width: 3px; height: 52px; background: #3d4249; }

  .intro { position: absolute; right: 55px; text-align: right; font-size: 13px; line-height: 15.5px; color: var(--grey-text); }
  .intro--first { top: 313px; width: 400px; }
  .intro--second { top: 365px; width: 560px; }
  .intro strong { color: var(--blue-head); font-weight: 700; font-size: 14px; }

  .services-title { position: absolute; left: 75px; top: 790px; color: var(--white); }
  .services-title__light { font-weight: 300; font-size: 27px; line-height: 28px; }
  .services-title__bold { font-weight: 700; font-size: 26px; line-height: 28px; }
  .services-title__bar { position: absolute; left: 55px; top: 796px; width: 3px; height: 44px; background: var(--white); }

  .service { position: absolute; color: var(--white); font-size: 13px; line-height: 15.5px; }
  .service::before {
    content: ""; position: absolute; left: -23px; top: 4px;
    width: 8px; height: 8px; background: var(--white);
  }
  .service--wide { left: 75px; top: 857px; width: 500px; }
  .service--left { left: 75px; top: 995px; width: 268px; }
  .service--right { left: 404px; top: 995px; width: 292px; }
</style>
</head>
<body>
<main class="flyer">
  <svg class="flyer__shapes" viewBox="0 0 936 1322" preserveAspectRatio="none" aria-hidden="false">
    <defs>
      <linearGradient id="techTop" x1="0" y1="0" x2="1" y2="1">
        <stop offset="0" stop-color="#b9bcc0"/>
        <stop offset="0.5" stop-color="#9aa3a8"/>
        <stop offset="1" stop-color="#7d8a6e"/>
      </linearGradient>
      <linearGradient id="techWrench" x1="0" y1="0" x2="1" y2="1">
        <stop offset="0" stop-color="#e8eef3"/>
        <stop offset="0.45" stop-color="#5b76a6"/>
        <stop offset="0.7" stop-color="#d7b43a"/>
        <stop offset="1" stop-color="#a9b3bd"/>
      </linearGradient>
      <linearGradient id="deal" x1="0" y1="0" x2="1" y2="1">
        <stop offset="0" stop-color="#bcd3ea"/>
        <stop offset="0.5" stop-color="#6f95c0"/>
        <stop offset="1" stop-color="#e7d27a"/>
      </linearGradient>
      <clipPath id="circleClip"><circle cx="307" cy="656" r="171"/></clipPath>
    </defs>

    <!-- top left: technician photo area -->
    <polygon points="0,0 612,0 262,336 0,110" fill="url(#techTop)" role="img" aria-label="Technician in hard hat and safety vest servicing a ceiling air-conditioning unit"/>
    <polygon points="0,70 0,385 160,240" fill="var(--blue-deep)"/>
    <polygon points="0,385 0,432 250,220 215,212" fill="var(--grey-band)"/>

    <!-- lower blue field -->
    <polygon points="0,851 682,476 936,476 936,1322 0,1322" fill="var(--blue-deep)"/>
    <polygon points="0,820 682,446 682,476 0,851" fill="var(--grey-band)"/>

    <!-- right photo with grey edge -->
    <polygon points="682,476 936,476 936,1215 488,742" fill="var(--grey-band)"/>
    <polygon points="682,476 936,476 936,1195 502,741" fill="url(#techWrench)" role="img" aria-label="Worker in yellow gloves tightening a pipe fitting with an adjustable wrench"/>

    <!-- bottom band -->
    <rect x="0" y="1293" width="936" height="5" fill="#0a3f7c"/>
    <rect x="0" y="1298" width="936" height="24" fill="var(--blue-mid)"/>

    <!-- circle photo -->
    <circle cx="307" cy="660" r="198" fill="#d8d9db"/>
    <circle cx="307" cy="656" r="193" fill="var(--white)"/>
    <g clip-path="url(#circleClip)">
      <rect x="130" y="480" width="360" height="360" fill="url(#deal)" role="img" aria-label="Business handshake over construction plans with a hard hat and a crane in the background"/>
    </g>
    <circle cx="307" cy="656" r="171" fill="none" stroke="var(--blue-mid)" stroke-width="2"/>
  </svg>

  <header class="headline">
    <div class="headline__lead">over <span class="headline__big">40 YEARS</span> of</div>
    <div class="headline__main">EXPERIENCE IN FACILITY</div>
    <div class="headline__sub">&amp; equipment maintenance,</div>
    <div class="headline__tag">let us show you the HFS difference!</div>
  </header>
  <div class="headline__rule"></div>

  <div class="section-title">
    <div class="section-title__light">Retail &amp; Commercial</div>
    <div class="section-title__bold">Maintenance Solutions</div>
  </div>
  <div class="section-title__bar"></div>

  <p class="intro intro--first">Harbor Facility Solutions knows how important it is to convert window shoppers to paying customers and to move inventory off your shelves.</p>
  <p class="intro intro--second">We ensure that your business is always looking its best with our <strong>cost-effective</strong> maintenance programs and crews available <strong>24/7</strong> to take care of any equipment or facility malfunction as quickly as possible.</p>

  <div class="services-title__bar"></div>
  <div class="services-title">
    <div class="services-title__light">Retail Maintenance Services</div>
    <div class="services-title__bold">You Can Rely On</div>
  </div>

  <p class="service service--wide">Harbor Facility Solutions provides services to stand-alone stores and big box stores alike, malls, nightclubs, and more. We work to enhance your image by taking preventative measures, like inspecting equipment for signs of wear or failing components. We service equipment as needed, measuring either by usage or manufacturer recommendations. After maintenance and repairs, our technicians provide an in-depth report on equipment conditions, analyze equipment failure, and discuss future prevention.</p>

  <p class="service service--left">Customers may not realize how much work and effort goes into maintaining a functional well-kept business, but Harbor Facility does. For your convenience, we offer a vast range of services to handle any issues that may occur or to help you expand your business, whether adding on to your existing location or moving to a new one.</p>

  <p class="service service--right">We install doors, restroom partitions, storefronts, flooring, and plumbing. Repairs include doors, storefronts, flooring, building exteriors, plumbing, appliances, fencing, and loading docks. We take care of landscaping, snow removal, irrigation systems, pest control, and other seasonal maintenance as need be when the weather changes.</p>
</main>
</body>
</html>
```